Membership Card Design

I need a basic membership card...it will entitle the customer to free entry to forthcoming promotions.
The business is called STARLANE PLAY and is a amusement arcade located in N Ireland.
I require .....
STARLANE PLAY MEMBER...across top of card in logo format.
Next line....this card entitles the holder free entry to forthcoming STARLANE EVENTS....
Then next line....customer name( space to write their name )
Next line.....customer mobile number ( space to write number )
On rear of card....logo/picture & STARLANE PLAY MEMBER written on back.

Industry/Entity Type

Business

Contact Information for Business Card

STARLANE PLAY
MEMBERSHIP CARD

```html
<!DOCTYPE html>
<html lang="en">
<head>
<meta charset="utf-8">
<title>Starlane Play Membership Card</title>
<link rel="stylesheet" href="https://fonts.googleapis.com/css2?family=Cinzel:wght@400;600;700&display=swap">
<style>
  :root {
    --canvas-bg: #c9c9c9;
    --canvas-bg-light: #e4e4e4;
    --card-black: #141414;
    --card-black-soft: #2a2a2a;
    --silver-light: #f2f2f2;
    --silver-mid: #cfcfcf;
    --silver-dark: #9a9a9a;
    --ink-white: #f5f5f5;
    --ink-grey: #6d6d6d;
  }
  * { margin: 0; padding: 0; box-sizing: border-box; }
  html, body { width: 1200px; height: 1023px; overflow: hidden; }
  body {
    background: radial-gradient(ellipse at 60% 35%, var(--canvas-bg-light), var(--canvas-bg) 75%);
    font-family: "Cinzel", serif;
    position: relative;
  }
  .card {
    position: absolute;
    width: 640px;
    height: 366px;
    border-radius: 6px;
    overflow: hidden;
    background: linear-gradient(135deg, var(--card-black-soft) 0%, var(--card-black) 45%, #000 100%);
    box-shadow: 0 18px 40px rgba(0,0,0,0.35);
    color: var(--ink-white);
  }
  .card-front { left: 80px; top: 90px; }
  .card-back { left: 480px; top: 567px; }

  .brand {
    position: absolute;
    display: flex;
    align-items: center;
    gap: 12px;
  }
  .brand-dot {
    width: 22px; height: 22px;
    border: 2px solid var(--ink-white);
    border-radius: 50%;
  }
  .brand-name {
    font-family: "Cinzel", serif;
    font-weight: 700;
    font-size: 32px;
    letter-spacing: 2px;
    color: var(--ink-white);
  }
  .card-front .brand { left: 42px; top: 40px; }

  .entitlement {
    position: absolute;
    left: 42px; top: 112px;
    font-size: 17px;
    line-height: 1.55;
    letter-spacing: 0.5px;
  }
  .entitlement strong { font-weight: 700; }
  .checkboxes {
    position: absolute;
    right: 40px; top: 112px;
    display: flex; gap: 10px; align-items: flex-end;
  }
  .checkbox { width: 26px; height: 22px; background: var(--silver-light); }

  .silver-band { position: absolute; left: 0; bottom: 0; width: 640px; height: 190px; }
  .fill-fields {
    position: absolute;
    left: 48px; bottom: 30px;
    color: var(--ink-grey);
    font-size: 18px;
    line-height: 2.1;
    letter-spacing: 0.5px;
  }

  .card-back .brand { left: 50%; top: 110px; transform: translateX(-50%); }
  .member-line {
    position: absolute;
    left: 0; right: 0; top: 240px;
    text-align: center;
    font-size: 26px;
    letter-spacing: 2px;
  }
</style>
</head>
<body>
  <section class="card card-front">
    <div class="brand">
      <span class="brand-dot"></span>
      <span class="brand-name">STARLANE PLAY</span>
    </div>
    <p class="entitlement">This card entitles the holder free entry<br>to forthcoming <strong>STARLANE EVENTS</strong></p>
    <div class="checkboxes">
      <svg class="checkbox" viewBox="0 0 26 22"><rect width="26" height="22" fill="#f2f2f2"/><path d="M6 11 L11 16 L20 5" stroke="#141414" stroke-width="2.5" fill="none"/></svg>
      <svg class="checkbox" viewBox="0 0 26 22"><rect width="26" height="22" fill="#f2f2f2"/><path d="M6 11 L11 16 L20 5" stroke="#141414" stroke-width="2.5" fill="none"/></svg>
      <span class="checkbox"></span>
    </div>
    <svg class="silver-band" viewBox="0 0 640 190" preserveAspectRatio="none">
      <defs>
        <linearGradient id="silverFill" x1="0" y1="0" x2="1" y2="1">
          <stop offset="0" stop-color="#f2f2f2"/>
          <stop offset="0.6" stop-color="#d6d6d6"/>
          <stop offset="1" stop-color="#a8a8a8"/>
        </linearGradient>
      </defs>
      <path d="M0 40 C220 -10 420 30 640 10 L640 190 L0 190 Z" fill="#5a5a5a"/>
      <path d="M0 52 C220 4 420 44 640 24 L640 190 L0 190 Z" fill="url(#silverFill)"/>
    </svg>
    <div class="fill-fields">
      <p>Customer Name :</p>
      <p>Customer Mobile Number :</p>
    </div>
  </section>

  <section class="card card-back">
    <div class="brand">
      <span class="brand-dot"></span>
      <span class="brand-name">STARLANE PLAY</span>
    </div>
    <p class="member-line">STARLANE PLAY MEMBER</p>
  </section>
</body>
</html>
```